BrightKeel Business Card Contest

We are looking for a modern business card that catches attention and is unique. Attached is the brand guide and logo files. Please note that the back side (not the side with our name and info) with be UV raise printed, so have fun with the design there. We want to include Name, Title, Phone number, email, website.

Contact Information for Business Card

Please see project description

```html
<!DOCTYPE html>
<html lang="en">
<head>
<meta charset="utf-8">
<title>BrightKeel Business Card</title>
<link rel="stylesheet" href="https://fonts.googleapis.com/css2?family=Outfit:wght@500&family=Montserrat:wght@400;700&display=swap">
<style>
  :root {
    --stage: #1c1c1c;
    --paper: #f4f4f4;
    --ink: #1f1f24;
    --navy: #1e2f6e;
    --orange: #e87d22;
    --red: #d52f27;
    --cyan: #1fa8dc;
    --blue: #2a7fc4;
    --deep-blue: #1b3a8a;
    --slate: #9fb6c8;
    --card-black: #151515;
    --pattern-grey: #8a8a8a;
    --white: #ffffff;
  }
  * { box-sizing: border-box; margin: 0; padding: 0; }
  html, body { width: 1200px; height: 1059px; overflow: hidden; }
  body { background: var(--stage); position: relative; font-family: "Montserrat", Arial, sans-serif; }

  .card {
    position: absolute;
    left: 255px;
    width: 690px;
    height: 392px;
    border-radius: 18px;
    overflow: hidden;
  }
  .card--front { top: 89px; background: var(--paper); }
  .card--back { top: 546px; background: var(--card-black); }

  .wordmark {
    position: absolute;
    font-family: "Outfit", Arial, sans-serif;
    font-weight: 500;
    letter-spacing: -0.5px;
    line-height: 1;
  }
  .card--front .wordmark { left: 42px; top: 52px; font-size: 54px; color: var(--ink); }

  .name-accent {
    position: absolute; left: 0; top: 182px; width: 20px; height: 42px;
    background: var(--orange);
  }
  .person-name {
    position: absolute; left: 43px; top: 178px;
    font-weight: 700; font-size: 25px; color: var(--navy); letter-spacing: 0.3px;
  }
  .person-title {
    position: absolute; left: 43px; top: 207px;
    font-size: 17px; color: var(--ink);
  }

  .contact-list { position: absolute; left: 42px; top: 268px; list-style: none; }
  .contact-list li {
    display: flex; align-items: center; height: 29px;
    font-size: 17px; color: var(--ink); letter-spacing: 0.2px;
  }
  .contact-list svg { width: 14px; height: 14px; margin-right: 8px; flex: none; }

  .brand-field {
    position: absolute; left: 390px; top: 40px; width: 268px; height: 268px;
    margin-top: 22px;
    background: linear-gradient(160deg, var(--red) 0%, var(--orange) 22%, var(--slate) 45%, var(--cyan) 65%, var(--blue) 80%, var(--deep-blue) 100%);
  }

  .back-pattern {
    position: absolute; inset: 0;
    background: linear-gradient(90deg, #0e0e0e 0%, #161616 35%, #3a3a3a 65%, var(--pattern-grey) 100%);
    opacity: 0.55;
  }
  .back-mark {
    position: absolute; left: 320px; top: 253px; width: 50px; height: 50px;
    background: var(--orange);
  }
  .card--back .wordmark { left: 386px; top: 251px; font-size: 48px; color: var(--white); }
</style>
</head>
<body>
  <section class="card card--front" aria-label="Business card front">
    <div class="wordmark">BrightKeel</div>
    <div class="name-accent"></div>
    <div class="person-name">DANIEL REYES</div>
    <div class="person-title">CEO/Founder</div>
    <ul class="contact-list">
      <li>
        <svg viewBox="0 0 16 16" aria-hidden="true"><path fill="var(--cyan)" d="M3.5 1.5l2.4 0.3 1 3-1.6 1.2a8 8 0 0 0 4.7 4.7l1.2-1.6 3 1 .3 2.4-2 1.8C6.9 14 2 9.1 1.7 3.5z"/></svg>
        (555) 214-7730
      </li>
      <li>
        <svg viewBox="0 0 16 16" aria-hidden="true"><rect x="1" y="4" width="14" height="10" rx="1" fill="var(--cyan)"/><path d="M1.5 4.5L8 9.5l6.5-5" fill="none" stroke="var(--paper)" stroke-width="1.3"/></svg>
        info@brightkeel.com
      </li>
      <li>
        <svg viewBox="0 0 16 16" aria-hidden="true"><circle cx="8" cy="8" r="7" fill="var(--cyan)"/><path d="M4 5c2 0 2 2 3 3s0 3 1 4M10 3c0 2 2 2 3 3" fill="none" stroke="var(--paper)" stroke-width="1.2"/></svg>
        www.brightkeel.com
      </li>
    </ul>
    <div class="brand-field" role="img" aria-label="Large faceted brand emblem in red, orange and blues"></div>
  </section>

  <section class="card card--back" aria-label="Business card back">
    <div class="back-pattern" role="img" aria-label="Raised UV pattern of repeated emblems fading from black to grey"></div>
    <div class="back-mark"></div>
    <div class="wordmark">BrightKeel</div>
  </section>
</body>
</html>
```